Web Based Ordering. We have an existing input screen- Need to Clean it up

we have an existing ordering Modal on a trucking management system, but it looks and feels clunky. We would like to modernize the look and feel of it. We need to keep the same input fields, but we are open to any type of reconfiguration or layout changes you can think of to improve the flow and layout.

This design is for a web browser, not mobile app.

Target Market(s)

construction and trucking industry

Colors
85acd3
3176b5
33a6d7
85cae6
33b8a4
86cfc6

Requirements
Must have
• all the input fields displayed are required
Nice to have
• some of the fields can probably be combined to consolidate the number of tabs.

```html
<!DOCTYPE html>
<html lang="en">
<head>
<meta charset="utf-8">
<title>New Material Order</title>
<link href="https://fonts.googleapis.com/css2?family=Poppins:wght@400;500;600;700&display=swap" rel="stylesheet">
<style>
:root{
  --brand:#0399dd;
  --bg:#efefef;
  --white:#ffffff;
  --ink:#000000;
  --text:#555555;
  --muted:#777777;
  --pill:#e8e8e8;
}
*{margin:0;padding:0;box-sizing:border-box}
html,body{width:1200px;height:1167px;overflow:hidden}
body{position:relative;background:var(--white);font-family:'Poppins',sans-serif;color:var(--text)}
.topbar{position:absolute;left:0;top:0;width:1200px;height:39px;background:var(--brand)}
.topbar h1{position:absolute;left:101px;top:9px;font-size:15.5px;font-weight:600;color:var(--white)}
.steps{position:absolute;left:101px;top:72px;display:flex;gap:3px}
.step{height:28px;padding:0 9px;border-radius:14px;background:var(--pill);font-size:12.5px;line-height:28px;color:#444}
.step.active{background:var(--brand);color:var(--white);padding:0 10px 0 12px}
.edit-icon{position:absolute;left:1083px;top:78px}
.main{position:absolute;left:0;top:137px;width:1200px;height:975px;background:var(--bg)}
.page-title{position:absolute;left:0;width:1200px;top:64px;text-align:center;font-size:50px;font-weight:700;color:var(--ink);line-height:1.3}
.label{position:absolute;font-size:12px;color:var(--muted)}
.field{position:absolute;height:45px;background:var(--white);border-radius:23px;box-shadow:0 3px 6px rgba(0,0,0,.08);font-size:11.5px;line-height:45px;padding-left:20px;color:var(--text)}
.field .ctrl{position:absolute;right:22px;top:0;font-size:10px;color:#777}
.truck-photo{position:absolute;left:498px;top:534px;width:216px;height:216px;border-radius:50%;background:linear-gradient(135deg,#b8b4dc 0%,#dcdde8 45%,#6a6a6a 100%)}
.btn-continue{position:absolute;left:435px;top:816px;width:330px;height:56px;border-radius:28px;background:var(--brand);color:var(--white);font-size:17px;font-weight:500;text-align:center;line-height:56px;box-shadow:0 6px 14px rgba(3,153,221,.3)}
.cancel{position:absolute;left:0;width:1200px;top:893px;text-align:center;font-size:12.5px;color:var(--muted)}
.footer-rule{position:absolute;left:0;top:1112px;width:1200px;height:6px;background:var(--brand)}
.copyright{position:absolute;left:0;top:1133px;width:1200px;text-align:center;font-size:12px;color:var(--muted)}
</style>
</head>
<body>
<header class="topbar"><h1>New Material Order</h1></header>
<nav class="steps">
  <span class="step active">Date and Start</span>
  <span class="step">Destination</span>
  <span class="step">Material</span>
  <span class="step">Trucks</span>
  <span class="step">Rates</span>
  <span class="step">Summary</span>
</nav>
<svg class="edit-icon" width="24" height="24" viewBox="0 0 24 24" aria-hidden="true">
  <path d="M4 17l11-11 3 3-11 11H4z" fill="#0399dd"/>
  <path d="M16 5l2-2 3 3-2 2z" fill="#0399dd"/>
  <rect x="2" y="21" width="20" height="2" fill="#0399dd"/>
</svg>
<main class="main">
  <h2 class="page-title">Date and Start</h2>
  <span class="label" style="left:244px;top:172px">Customer *</span>
  <div class="field" style="left:239px;top:198px;width:723px">R.J. Harlow Paving Company, Inc.<span class="ctrl">x &nbsp;&nbsp;⌄</span></div>
  <span class="label" style="left:244px;top:271px">Starting Location *</span>
  <div class="field" style="left:240px;top:298px;width:722px">2109-Linwood US 12/SR 8<span class="ctrl">x &nbsp;&nbsp;⌄</span></div>
  <span class="label" style="left:244px;top:373px">Load Date *</span>
  <div class="field" style="left:240px;top:400px;width:345px">02/27/2021<span class="ctrl" style="right:24px">x</span></div>
  <span class="label" style="left:621px;top:373px">Load Time *</span>
  <div class="field" style="left:617px;top:400px;width:346px;padding-left:14px">6:00 AM</div>
  <div class="truck-photo" role="img" aria-label="Photo of a white semi truck with trailer on the road"></div>
  <div class="btn-continue">Continue</div>
  <div class="cancel">Cancel</div>
</main>
<div class="footer-rule"></div>
<p class="copyright">Copyright © 2021. All rights reserved.</p>
</body>
</html>
```